Design for "Vellow" protein health bars wrappers

I need a new design for a protein bar that my partners and I are launching for the North American and European markets.
The bar's name is "Vellow."
Given the masculine/aggressive nature of that name, we are thinking of neutralizing it with a more feminine/soft font and design. But hey - the sky is the limit. We obviously want this 20-gram protein bar to sell to a wide net (not just men but women also). So if it means having a Pellam Comic font/design (or whatever) in order to do this, so be it. I leave it up to your intelligence and experience.

ADDED ON FEBRUARY 24:

The official name of the bar is just "VELLOW" (not "Vellow Protein").

We have six flavors divided into two categories, which are 1) SOFT and 2) CRUNCHY.
So, the idea is to make two similar designs for the wrapper that still distinguish themselves from each other because one is 'soft' and the other is 'crunchy.'
Then, within each category, the idea is to have three color variations, designating the three flavors in each category.

Please look at the dimensions and examples of the generic wrapper designs that we already have (and which we find too generic), which I have uploaded.

Target Market(s)

North America - Brindle, Fair Harvest
Europe - Norway, Sweden, Denmark, Germany, France, Switzerland, Italy.

Industry/Entity Type

Nutrition

Logo Text

Vellow

Font styles to use
Serif
Decorative

Colors
fff6dc
f04a50

Requirements
Must have
• The title is "Vellow".
• We have six flavors divided into two categories, which are 1) SOFT and 2) CRUNCHY.
• You can work on the two different types of similar-but-different designs for the "soft" and for the "cruncy." Then it's just a question of color variations for each flavor.
• The flavors are:
• SOFT: 1) strawberry, 2) Chocolate brownie, 3) Cinnamon Crunch
• CRUNCY: 1) Peanut, 2) Lemon, 3) Coconut.
• On the side or at the bottom, there should be stated:
• "20 gm protein"
• "children friendly"
Nice to have
• Obvious: a design that catches the eye and inspires someone to buy the bar to eat it.
• Part of the design could include a photograph of the actual bar (you can use generic photos for that until we place a pic of the actual bar). Like 1/4th of the total surface (or even a little smaller).

```html
<!DOCTYPE html>
<html lang="en">
<head>
<meta charset="utf-8">
<title>Vellow – Chocolate brownie wrapper</title>
<link rel="stylesheet" href="https://fonts.googleapis.com/css2?family=Yellowtail&family=Roboto+Slab:wght@700&display=swap">
<style>
  :root {
    --stage: #dcdcdc;
    --cocoa: #73392c;
    --cocoa-deep: #562820;
    --tangerine: #f47a3a;
    --tangerine-light: #fbab72;
    --cream: #ffffff;
    --photo-dark: #3b1c14;
    --photo-mid: #6b3a2a;
    --photo-mint: #9cc8b4;
  }
  * { box-sizing: border-box; margin: 0; padding: 0; }
  html, body {
    width: 1200px;
    height: 752px;
    overflow: hidden;
    background: var(--stage);
  }
  .wrapper {
    position: absolute;
    left: 40px;
    top: 186px;
    width: 1120px;
    height: 380px;
  }
  .wrapper-art {
    position: absolute;
    inset: 0;
    width: 1120px;
    height: 380px;
  }
  .brand-name {
    position: absolute;
    left: 130px;
    top: 40px;
    font-family: "Roboto Slab", Georgia, serif;
    font-weight: 700;
    font-size: 128px;
    line-height: 1;
    letter-spacing: 1px;
    color: var(--cream);
    white-space: nowrap;
  }
  .flavor-name {
    position: absolute;
    left: 132px;
    top: 208px;
    font-family: "Yellowtail", cursive;
    font-size: 52px;
    line-height: 1;
    color: var(--cream);
    white-space: nowrap;
  }
  .claim {
    position: absolute;
    top: 324px;
    font-family: "Roboto Slab", Georgia, serif;
    font-weight: 700;
    font-size: 19px;
    letter-spacing: 0.5px;
    color: var(--cream);
    white-space: nowrap;
  }
  .claim-protein { left: 138px; }
  .claim-kids { left: 430px; }
</style>
</head>
<body>
  <div class="wrapper">
    <svg class="wrapper-art" viewBox="0 0 1120 380" xmlns="http://www.w3.org/2000/svg">
      <defs>
        <linearGradient id="cocoa-field" x1="0" y1="0" x2="0" y2="1">
          <stop offset="0" stop-color="var(--cocoa)"/>
          <stop offset="1" stop-color="var(--cocoa-deep)"/>
        </linearGradient>
        <linearGradient id="claim-band" x1="0" y1="0" x2="1" y2="0">
          <stop offset="0" stop-color="var(--tangerine)"/>
          <stop offset="0.5" stop-color="var(--tangerine-light)"/>
          <stop offset="1" stop-color="var(--tangerine)"/>
        </linearGradient>
        <linearGradient id="bar-photo-tone" x1="0" y1="0" x2="0" y2="1">
          <stop offset="0" stop-color="var(--photo-mid)"/>
          <stop offset="0.45" stop-color="var(--photo-dark)"/>
          <stop offset="0.62" stop-color="var(--photo-mint)"/>
          <stop offset="0.72" stop-color="var(--photo-dark)"/>
          <stop offset="1" stop-color="var(--photo-mid)"/>
        </linearGradient>
      </defs>

      <rect class="field" x="0" y="0" width="1120" height="380" fill="url(#cocoa-field)"/>

      <rect class="claim-band" x="0" y="300" width="1120" height="70" fill="url(#claim-band)"/>
      <rect class="base-edge" x="0" y="370" width="1120" height="10" fill="var(--cocoa-deep)"/>

      <path class="photo-frame" d="M800 0 Q 700 160 740 380 L1120 380 L1120 0 Z" fill="var(--tangerine)"/>
      <path class="bar-photo" role="img" aria-label="Photo of a chocolate brownie bar with mint layer"
            d="M822 0 Q 728 160 764 380 L1120 380 L1120 0 Z" fill="url(#bar-photo-tone)"/>

      <g class="seal seal-left" fill="var(--cocoa-deep)" opacity="0.55">
        <rect x="0" y="0" width="70" height="380"/>
      </g>
      <g class="seal-lines" stroke="var(--tangerine-light)" stroke-width="3" opacity="0.55">
        <line x1="16" y1="0" x2="16" y2="380"/>
        <line x1="32" y1="0" x2="32" y2="380"/>
        <line x1="48" y1="0" x2="48" y2="380"/>
        <line x1="64" y1="0" x2="64" y2="380"/>
        <line x1="1056" y1="0" x2="1056" y2="380"/>
        <line x1="1072" y1="0" x2="1072" y2="380"/>
        <line x1="1088" y1="0" x2="1088" y2="380"/>
        <line x1="1104" y1="0" x2="1104" y2="380"/>
      </g>
    </svg>

    <div class="brand-name">VELLOW</div>
    <div class="flavor-name">Chocolate brownie</div>
    <div class="claim claim-protein">20 GM PROTEIN</div>
    <div class="claim claim-kids">CHILDREN FRIENDLY</div>
  </div>
</body>
</html>
```